HVAC Contractor Website Design

We are working with an HVAC contractor in Idaho called KR HVAC.
Some sites to use for content/competitors and inspiration:
https://www.brelvoclimate.com
https://pinemarsh.site/web/contractor/ (lots of contractor website designs we've approved and continue to show clients)
Thank you for taking the time to consider designing a website for us. We are web developers based in Stockton, CA, USA. Most of our projects go through the same process. Understanding this process may help you win a project with us. We custom-code all of our websites in-house. We don’t have any requirements as to what tools you use for your design, but we prefer Figma files. For any design that we label as four-stars, we send it to the client for review. The client picks the final design they want us to use. Once we complete this process, we will continue to show additional clients all the four-star sites and purchase them later. Your designs will have multiple chances to sell. For better chances of success, we ask that you follow these guidelines.
IMAGES:
If you use any images or icons in the design, we ask that you have a link to the asset so we can purchase the image/icon. Most of the designs we submit do not have the customer’s images on them unless they have some great images. Be creative; show us the feeling you are trying to portray with your image choices. Use any royalty-free site you choose. We subscribe to Adobe and mainly use their images, but we can purchase images outside of Adobe.
PLEASE NOTE: we will not submit designs to clients with watermarks on the images.
FONTS:
We ask that you identify the fonts used in the design. This can be done in a message if you want. We typically use Google Fonts and Adobe Fonts.
CONTENT:
We're always open to different content and ideas. We often submit designs with stock images so the client can see our vision. We typically take pictures after the website launch to use their images with our vision. Lorem Ipsum is fine for paragraphs, but we ask that you write the headers in correct English. We want to be able to show the vision and identify the sections of the website.
INSPIRATION:
We typically add a couple of links in the brief of websites we like to help you get started in your design.
REVISIONS:
We do not often ask for revisions of the designs unless we see something in the design that may not appeal to the client. If there are slight changes that we want to make, we do that in the development process.
FEEDBACK:
We rarely give feedback on designs during the design process. We are working on many website projects and do not have the time to provide feedback. We usually respond if your request is well thought out and asks specific questions, but a note asking “feedback, please” usually goes unanswered

```html
<!DOCTYPE html>
<html lang="en">
<head>
<meta charset="utf-8">
<title>KR HVAC – Professional HVAC Services</title>
<link rel="stylesheet" href="https://fonts.googleapis.com/css2?family=Montserrat:wght@400;500;600;700;800&display=swap">
<style>
:root{
  --blue:#1a9fe3;
  --blue-dark:#1474c4;
  --orange:#ff5a10;
  --orange-deep:#e8400c;
  --ink:#111318;
  --text:#4b4f58;
  --muted:#8a8f98;
  --white:#ffffff;
  --black:#000000;
  --card-shadow:0 6px 22px rgba(0,0,0,.09);
}
*{box-sizing:border-box;margin:0;padding:0}
html,body{width:1200px;height:4335px;overflow:hidden;background:var(--white)}
body{position:relative;font-family:'Montserrat',sans-serif;color:var(--ink)}
.abs{position:absolute}
.btn{position:absolute;background:var(--orange);color:var(--white);font-size:16px;font-weight:500;display:flex;align-items:center;justify-content:center;letter-spacing:.3px}
.accent-blue{color:var(--blue)}
.accent-orange{color:var(--orange)}

/* header */
.topbar{left:278px;top:0;width:922px;height:37px;background:linear-gradient(90deg,var(--blue),var(--blue-dark));color:var(--white);font-size:15px;display:flex;align-items:center}
.topbar .item{position:absolute;display:flex;align-items:center;gap:8px}
.social-dot{position:absolute;width:16px;height:16px;border-radius:50%;background:var(--white)}
.brand{left:46px;top:24px;font-size:44px;font-weight:800;color:var(--ink);letter-spacing:-1px;display:flex;align-items:center;gap:10px}
.brand .mark{width:14px;height:14px;border-radius:50%;background:var(--orange)}
.nav{top:64px;font-size:17px;font-weight:500;color:var(--ink)}
.header-line{left:0;top:108px;width:1200px;height:2px;background:#e3e5e8}

/* hero */
.hero-photo{left:0;top:110px;width:1200px;height:705px;background:linear-gradient(100deg,#eef0f2 0%,#e4e7ea 40%,#b8c7d6 62%,#3f6fb3 80%,#2b4c86 100%)}
.hero-kicker{left:65px;top:240px;font-size:30px;font-weight:500;color:var(--blue)}
.hero-title{left:64px;top:288px;font-size:56px;font-weight:800;line-height:66px;color:var(--ink)}
.hero-copy{left:68px;top:430px;font-size:15px;line-height:19px;color:var(--ink)}
.dot{position:absolute;top:669px;width:19px;height:19px;border-radius:50%;border:2px solid var(--blue)}
.dot.on{background:var(--blue)}

/* about */
.about-photo{left:79px;top:931px;width:501px;height:417px;background:linear-gradient(135deg,#6f6e6a,#b9b8b3 45%,#d8d9db 70%,#4e4c49);clip-path:polygon(0 0,100% 0,86% 100%,0 100%)}
.section-title{font-size:48px;font-weight:800;color:var(--ink)}
.about-copy{left:627px;top:1082px;width:530px;font-size:18px;line-height:28px;color:var(--text)}

/* services */
.services-band{left:0;top:1492px;width:1200px;height:445px;background:linear-gradient(120deg,#0f71c6 0%,#2c87d6 40%,#4d8fd4 70%,#3567b9 100%)}
.service-card{position:absolute;top:1742px;width:190px;height:189px;background:var(--blue);color:var(--white);text-align:center;font-size:14px;font-weight:700;line-height:16px}
.service-card .icon{position:absolute;left:40px;top:15px;width:110px;height:110px;border-radius:50%;background:var(--white);display:flex;align-items:center;justify-content:center}
.service-card .label{position:absolute;left:0;right:0;top:146px}
.arrow{position:absolute;width:38px;height:36px;background:var(--blue);display:flex;align-items:center;justify-content:center}

/* testimonials */
.review{position:absolute;top:2185px;width:310px;height:156px;background:var(--white);box-shadow:var(--card-shadow);padding:20px 20px 0 20px}
.stars{color:#e8221b;font-size:18px;letter-spacing:3px;line-height:18px}
.review p{margin-top:10px;font-size:13px;line-height:20px;color:var(--muted)}
.reviewer{position:absolute;top:2370px;display:flex;align-items:center;gap:14px}
.avatar{width:58px;height:58px;border-radius:50%;background:linear-gradient(135deg,#9a948c,#4d4a46)}
.reviewer .name{font-size:14px;font-weight:600;color:#1d2250}
.reviewer .role{font-size:10px;font-weight:500;color:#e8221b;margin-top:4px}

/* quote */
.quote-band{left:0;top:2580px;width:1200px;height:470px;background:linear-gradient(100deg,#d8360f 0%,#f04a12 35%,#ff6a1a 60%,#ff9a3c 85%,#ffb25a 100%)}
.quote-title{left:0;width:1200px;top:2632px;text-align:center;font-size:48px;font-weight:800;color:var(--white)}
.field{position:absolute;background:var(--white);border:2px solid #d6d6d6;font-size:13px;color:#333;padding-left:28px;display:flex;align-items:center}

/* blog */
.post-photo{position:absolute;top:3267px;width:298px;height:212px}
.post-title{position:absolute;top:3500px;width:290px;font-size:17px;font-weight:600;line-height:21px;color:var(--ink)}
.post-meta{position:absolute;top:3557px;font-size:11px;color:var(--muted)}
.read-more{position:absolute;top:3599px;font-size:16px;font-weight:500;color:var(--blue)}

/* footer */
.footer-heading{position:absolute;top:3968px;font-size:21px;font-weight:600;color:var(--white)}
.footer-link{position:absolute;font-size:14px;color:#c9c9c9}
.footer-social{position:absolute;top:4106px;width:24px;height:24px;border-radius:50%;background:var(--blue)}
.footer-rule{left:60px;top:4278px;width:1096px;height:1px;background:#3a3a3a}
.copyright{left:0;top:4302px;width:1200px;text-align:center;font-size:14px;color:#d6d6d6}
</style>
</head>
<body>

<!-- header -->
<div class="abs topbar">
  <div class="item" style="left:40px">
    <svg width="14" height="11" viewBox="0 0 14 11"><rect x="0.5" y="0.5" width="13" height="10" fill="none" stroke="#fff"/><path d="M1 1l6 5 6-5" fill="none" stroke="#fff"/></svg>
    info@website.com
  </div>
  <div class="item" style="left:258px">
    <svg width="13" height="13" viewBox="0 0 24 24"><path fill="#fff" d="M6.6 10.8a15 15 0 006.6 6.6l2.2-2.2c.3-.3.7-.4 1-.2 1.1.4 2.3.6 3.6.6.6 0 1 .4 1 1V20c0 .6-.4 1-1 1A17 17 0 013 4c0-.6.4-1 1-1h3.5c.6 0 1 .4 1 1 0 1.3.2 2.5.6 3.6.1.3 0 .7-.2 1z"/></svg>
    (123) 456 7890
  </div>
  <span class="social-dot" style="left:790px"></span>
  <span class="social-dot" style="left:818px"></span>
  <span class="social-dot" style="left:846px"></span>
</div>
<div class="abs brand">KR HVAC<span class="mark"></span></div>
<div class="abs nav" style="left:323px">HOME</div>
<div class="abs nav" style="left:418px">ABOUT</div>
<div class="abs nav" style="left:523px">SERVICES</div>
<div class="abs nav" style="left:657px">REVIEWS</div>
<div class="abs nav" style="left:788px">CONTACT US</div>
<div class="btn" style="left:1008px;top:56px;width:153px;height:38px">GET A QUOTE</div>
<div class="abs header-line"></div>

<!-- hero -->
<div class="abs hero-photo" role="img" aria-label="Technician in a blue cap servicing a wall-mounted air conditioner"></div>
<svg class="abs" style="left:0;top:660px" width="1200" height="190" viewBox="0 0 1200 190">
  <polygon points="0,150 1200,115 1200,190 0,190" fill="#fff"/>
  <polygon points="0,20 1200,115 1200,155 0,50" fill="#fff"/>
  <polygon points="0,20 1200,112 1200,153 0,44" fill="url(#heroStripe)"/>
  <defs><linearGradient id="heroStripe" x1="0" x2="1"><stop offset="0" stop-color="#e8300c"/><stop offset="1" stop-color="#ff7a14"/></linearGradient></defs>
</svg>
<div class="abs hero-kicker">WELCOME TO KR HVAC</div>
<div class="abs hero-title">PROFESSIONAL<br><span class="accent-orange">HVAC</span> SERVICES</div>
<div class="abs hero-copy">Lorem ipsum dolor sit amet, consectetuer adipiscing elit.<br>Aenean commodo ligula eget dolor.</div>
<div class="btn" style="left:64px;top:494px;width:153px;height:38px">GET A QUOTE</div>
<span class="dot" style="left:614px"></span>
<span class="dot on" style="left:647px"></span>
<span class="dot" style="left:679px"></span>

<!-- about -->
<div class="abs about-photo" role="img" aria-label="Technician repairing an outdoor condenser unit on a rooftop"></div>
<svg class="abs" style="left:500px;top:931px" width="82" height="417" viewBox="0 0 82 417"><line x1="80" y1="0" x2="8" y2="417" stroke="#ff5a10" stroke-width="5" stroke-dasharray="22 8"/></svg>
<div class="abs section-title" style="left:627px;top:1004px">ABOUT <span class="accent-blue">US</span></div>
<div class="abs about-copy">Lorem ipsum dolor sit amet, consectetur adipiscing elit, sed do eiusmod tempor incididunt ut labore et dolore magna aliqua. Ut enim ad minim veniam, quis nostrud exercitation ullamco laboris nisi ut aliquip ex ea commodo consequat. Duis aute irure dolor in reprehenderit in voluptate velit esse cillum dolore eu fugiat nulla pariatur.</div>
<div class="btn" style="left:627px;top:1285px;width:153px;height:38px">GET A QUOTE</div>

<!-- services -->
<div class="abs services-band" role="img" aria-label="Technician working on ceiling ductwork, tinted blue"></div>
<div class="abs section-title" style="left:0;width:1200px;top:1563px;text-align:center;color:#fff">OUR <span class="accent-blue" style="color:#3fb3f5">SERVICES</span></div>

<div class="arrow" style="left:20px;top:1828px"><svg width="14" height="18" viewBox="0 0 14 18"><path d="M10 2L3 9l7 7" fill="none" stroke="#fff" stroke-width="3"/></svg></div>
<div class="arrow" style="left:1134px;top:1838px"><svg width="14" height="18" viewBox="0 0 14 18"><path d="M4 2l7 7-7 7" fill="none" stroke="#fff" stroke-width="3"/></svg></div>

<div class="service-card" style="left:84px">
  <div class="icon"><svg width="72" height="50" viewBox="0 0 72 50" fill="none" stroke="#ff5a10" stroke-width="3"><rect x="2" y="4" width="68" height="24" rx="4"/><line x1="8" y1="20" x2="64" y2="20"/><path d="M22 36v8M30 36v10M38 36v8M46 36v10M54 36v8"/></svg></div>
  <div class="label">Air<br>Conditioning</div>
</div>
<div class="service-card" style="left:294px">
  <div class="icon"><svg width="62" height="70" viewBox="0 0 62 70" fill="none" stroke="#ff5a10" stroke-width="3"><circle cx="16" cy="26" r="8"/><path d="M16 8v6M16 38v6M2 26h6M24 26h6M6 16l4 4M6 36l4-4"/><path d="M36 46V10a6 6 0 0112 0v36"/><circle cx="42" cy="54" r="10"/><path d="M52 16h6M52 24h6M52 32h6"/></svg></div>
  <div class="label" style="top:150px">Heating</div>
</div>
<div class="service-card" style="left:503px">
  <div class="icon"><svg width="64" height="64" viewBox="0 0 64 64" fill="none" stroke="#ff5a10" stroke-width="3"><path d="M8 56L40 24"/><path d="M40 24a12 12 0 1016-16l-8 8-6-2-2-6 8-8"/><path d="M10 8l20 20M6 14l8-8M34 34l22 22-4 4-22-22"/></svg></div>
  <div class="label">Repairs &amp;<br>Installation</div>
</div>
<div class="service-card" style="left:713px">
  <div class="icon"><svg width="66" height="60" viewBox="0 0 66 60" fill="none" stroke="#ff5a10" stroke-width="3"><path d="M2 40V20h40v20z"/><path d="M10 20v-8h8v8M26 20V4h8v16"/><path d="M42 24c12 0 18 6 18 18v4H48v-4c0-4-2-6-6-6"/><path d="M50 50v8M54 50v8M58 50v8"/></svg></div>
  <div class="label">Duct<br>Cleaning</div>
</div>
<div class="service-card" style="left:922px">
  <div class="icon"><svg width="52" height="72" viewBox="0 0 52 72" fill="none" stroke="#ff5a10" stroke-width="3"><rect x="2" y="2" width="48" height="60" rx="4"/><rect x="12" y="10" width="28" height="22"/><path d="M26 14c4 5 6 8 6 11a6 6 0 01-12 0c0-3 2-6 6-11z"/><circle cx="26" cy="46" r="6"/><path d="M20 62v8M32 62v8"/></svg></div>
  <div class="label">Heat<br>Pumps</div>
</div>

<!-- testimonials -->
<div class="abs section-title" style="left:0;width:1200px;top:2064px;text-align:center">WHAT CLIENT <span class="accent-blue">SAYS</span></div>

<div class="review" style="left:98px"><div class="stars">★★★★★</div><p>Egestas fringilla phasellus faucibus scelerisque. Massa tincidunt dui ut ornare lectus. Elit ullamcorper dignissim cras tincidunt lobortis feugiat vivamus at.</p></div>
<div class="review" style="left:448px"><div class="stars">★★★★★</div><p>Egestas fringilla phasellus faucibus scelerisque. Massa tincidunt dui ut ornare lectus. Elit ullamcorper dignissim cras tincidunt lobortis feugiat vivamus at.</p></div>
<div class="review" style="left:801px"><div class="stars">★★★★★</div><p>Egestas fringilla phasellus faucibus scelerisque. Massa tincidunt dui ut ornare lectus. Elit ullamcorper dignissim cras tincidunt lobortis feugiat vivamus at.</p></div>

<div class="reviewer" style="left:112px"><div class="avatar" role="img" aria-label="Customer portrait"></div><div><div class="name">Dana R. Holloway</div><div class="role">CUSTOMER</div></div></div>
<div class="reviewer" style="left:458px"><div class="avatar" role="img" aria-label="Customer portrait"></div><div><div class="name">Dana R. Holloway</div><div class="role">CUSTOMER</div></div></div>
<div class="reviewer" style="left:818px"><div class="avatar" role="img" aria-label="Customer portrait"></div><div><div class="name">Dana R. Holloway</div><div class="role">CUSTOMER</div></div></div>

<!-- quote -->
<div class="abs quote-band" role="img" aria-label="Technician at an indoor unit, tinted orange"></div>
<div class="abs quote-title">REQUEST A QUOTE</div>
<div class="field" style="left:197px;top:2747px;width:243px;height:41px">NAME</div>
<div class="field" style="left:480px;top:2747px;width:243px;height:41px">EMAIL</div>
<div class="field" style="left:766px;top:2747px;width:243px;height:41px">PHONE NUMBER</div>
<div class="field" style="left:197px;top:2814px;width:811px;height:104px;align-items:flex-start;padding-top:26px">YOUR MESSAGE</div>
<div class="btn" style="left:197px;top:2961px;width:152px;height:39px">GET A QUOTE</div>

<!-- blog -->
<div class="abs section-title" style="left:0;width:1200px;top:3148px;text-align:center">LATEST FROM <span class="accent-blue">BLOG</span></div>

<div class="post-photo" style="left:109px;background:linear-gradient(135deg,#2a3a5a,#6f8fb3 50%,#c9b59c)" role="img" aria-label="Gloved hands tightening a pipe with pliers"></div>
<div class="post-photo" style="left:453px;background:linear-gradient(180deg,#3f7fd6,#9bbbe6 55%,#b08a52)" role="img" aria-label="State capitol building under a blue sky"></div>
<div class="post-photo" style="left:796px;background:linear-gradient(135deg,#8a8e95,#d9dbde 50%,#c7a98c)" role="img" aria-label="Technician inspecting a ceiling vent"></div>

<div class="post-title" style="left:124px">High-performance IT for manufacturing companies</div>
<div class="post-title" style="left:474px">A practical approach to business transformation</div>
<div class="post-title" style="left:822px;top:3504px">Real-world solutions for unprecedented challenges</div>

<div class="post-meta" style="left:127px">May 20, 2024</div><div class="post-meta" style="left:262px">No Comment</div>
<div class="post-meta" style="left:474px">May 20, 2024</div><div class="post-meta" style="left:608px">No Comment</div>
<div class="post-meta" style="left:822px">May 20, 2024</div><div class="post-meta" style="left:957px">No Comment</div>

<div class="read-more" style="left:127px">READ MORE</div>
<div class="read-more" style="left:474px">READ MORE</div>
<div class="read-more" style="left:822px">READ MORE</div>

<div class="btn" style="left:525px;top:3682px;width:153px;height:38px">VIEW ALL</div>

<!-- footer -->
<svg class="abs" style="left:0;top:3760px" width="1200" height="575" viewBox="0 0 1200 575">
  <defs><linearGradient id="footStripe" x1="0" x2="1"><stop offset="0" stop-color="#ff7a14"/><stop offset="1" stop-color="#e8300c"/></linearGradient></defs>
  <polygon points="0,40 1200,150 1200,575 0,575" fill="#000"/>
  <polygon points="0,10 1200,110 1200,145 0,40" fill="url(#footStripe)"/>
</svg>
<div class="abs brand" style="left:44px;top:3993px;color:#fff;font-size:50px">KR HVAC<span class="mark"></span></div>
<span class="footer-social" style="left:44px"></span>
<span class="footer-social" style="left:105px"></span>
<span class="footer-social" style="left:169px"></span>

<div class="footer-heading" style="left:429px">Company</div>
<div class="footer-link" style="left:440px;top:4023px">Home</div>
<div class="footer-link" style="left:440px;top:4063px">About</div>
<div class="footer-link" style="left:440px;top:4100px">Services</div>
<div class="footer-link" style="left:440px;top:4144px">Blog</div>
<div class="footer-link" style="left:440px;top:4191px">Contact</div>

<div class="footer-heading" style="left:653px">Quick Links</div>
<div class="footer-link" style="left:664px;top:4023px">FAQS</div>
<div class="footer-link" style="left:664px;top:4063px">Privacy Policy</div>
<div class="footer-link" style="left:664px;top:4100px">Term &amp; Conditions</div>
<div class="footer-link" style="left:664px;top:4144px">Cookie Policy</div>
<div class="footer-link" style="left:664px;top:4191px">Get a Quote</div>

<div class="footer-heading" style="left:909px;top:3966px">Contact Info</div>
<svg class="abs" style="left:914px;top:4023px" width="18" height="18" viewBox="0 0 24 24"><path fill="#1a9fe3" d="M6.6 10.8a15 15 0 006.6 6.6l2.2-2.2c.3-.3.7-.4 1-.2 1.1.4 2.3.6 3.6.6.6 0 1 .4 1 1V20c0 .6-.4 1-1 1A17 17 0 013 4c0-.6.4-1 1-1h3.5c.6 0 1 .4 1 1 0 1.3.2 2.5.6 3.6.1.3 0 .7-.2 1z"/></svg>
<div class="footer-link" style="left:945px;top:4023px">+1 208 555 0147</div>
<svg class="abs" style="left:914px;top:4068px" width="19" height="15" viewBox="0 0 19 15"><rect x="0" y="2" width="19" height="13" fill="#1a9fe3"/><path d="M0 2l9.5 7L19 2" fill="none" stroke="#000" stroke-width="1.5"/></svg>
<div class="footer-link" style="left:945px;top:4066px">help@krhvac-mail.com</div>
<svg class="abs" style="left:914px;top:4112px" width="16" height="22" viewBox="0 0 16 22"><path fill="#1a9fe3" d="M8 0a8 8 0 00-8 8c0 6 8 14 8 14s8-8 8-14a8 8 0 00-8-8zm0 11a3 3 0 110-6 3 3 0 010 6z"/></svg>
<div class="footer-link" style="left:945px;top:4108px;line-height:22px">418 Cedar Ridge Ave, Suite 12 -<br>Boise, ID 83702</div>

<div class="abs footer-rule"></div>
<div class="abs copyright">© 2024 Northpine Studio. All Rights Reserved.</div>

</body>
</html>
```